Poster Design - Stand Up Paddle Eco Tour

We need a A3 size poster design (using Adobe Illustrator) for our company's stand up paddle tour. Our tour is on flat water, calm and safe, suitable for all ages and level.

WE provide worldclass SUP boards for our customers. And branded Joren Maltby life jacket. Our instructors are all well trained and exeprience. Plus they are super friendly. Every paddling trip come with a safety boat.

Please refer to attached files for text and photos.

Our website is www.brinkwaveoar.com.sg

IMPORTANT NOTE - The design has to be done in Adobe Illustrator. The winning designer has to submit the working file in Adobe Illustrator.

Target Market(s)

Working adult - 20 - 35 year old

Industry/Entity Type

Tourism

Requirements
Must have
• The project MUST be done in Adobe Illustrator and the winning designer has to submit the artwork to us in Adobe Illustrator format.
Nice to have
• pleasant to look at.

```html
<!DOCTYPE html>
<html lang="en">
<head>
<meta charset="utf-8">
<title>Brinkwave Oar – SUP Adventure Tour Poster</title>
<link rel="stylesheet" href="https://fonts.googleapis.com/css2?family=Oswald:wght@300;500&family=Open+Sans:wght@400;600;700&display=swap">
<style>
  :root{
    --navy:#15315f;
    --blue:#1f6fb5;
    --sky:#8fc3e6;
    --ink:#1d3f73;
    --white:#ffffff;
    --paper:#ffffff;
  }
  *{margin:0;padding:0;box-sizing:border-box}
  html,body{width:849px;height:1200px;overflow:hidden;background:var(--paper)}
  .poster{position:relative;width:849px;height:1200px;background:var(--paper);font-family:"Open Sans",sans-serif;color:var(--ink)}
  .hero{position:absolute;left:0;top:120px;width:849px;height:440px;
    background:linear-gradient(180deg,#cfe3f1 0%,#b9d4e6 35%,#7e98a3 48%,#8aa3ac 60%,#6f8791 100%)}
  .header-wave{position:absolute;left:0;top:0;width:849px;height:210px}
  .brand{position:absolute;left:0;right:0;top:38px;display:flex;justify-content:center;align-items:center;gap:10px}
  .brand-mark{width:22px;height:22px;border-radius:50%;background:var(--navy)}
  .brand-name{font-family:"Open Sans",sans-serif;font-weight:700;font-size:26px;letter-spacing:2px;color:var(--navy)}
  .headline{position:absolute;left:40px;right:40px;top:420px;text-align:center;color:var(--white);
    font-family:"Oswald",sans-serif;font-weight:300;font-size:35px;line-height:1.22;letter-spacing:.5px;text-transform:uppercase}
  .headline strong{font-weight:500}
  .intro{position:absolute;left:70px;right:70px;top:585px;text-align:center;font-size:17px;line-height:1.5;color:var(--ink)}
  .intro p+p{margin-top:20px}
  .gallery{position:absolute;left:42px;right:42px;top:752px;display:flex;gap:12px}
  .gallery .photo{flex:1;height:178px}
  .p1{background:linear-gradient(180deg,#6f8f6a 0%,#486a4c 45%,#8fa7a8 70%,#6e8a8c 100%)}
  .p2{background:linear-gradient(180deg,#a9c7e2 0%,#d9e7f1 40%,#9fb4bf 65%,#7f98a3 100%)}
  .p3{background:linear-gradient(180deg,#9fc0dd 0%,#5f8455 40%,#7e9aa5 62%,#67818a 100%)}
  .details{position:absolute;left:60px;right:60px;top:958px;text-align:center;font-size:17px;line-height:1.55;color:var(--ink)}
  .details b{font-weight:700}
  .contact-bar{position:absolute;left:0;top:1046px;width:849px;height:46px;background:var(--navy);
    color:var(--white);font-weight:700;font-size:21px;text-align:center;line-height:46px;letter-spacing:.5px;text-transform:uppercase}
  .footer{position:absolute;left:0;right:0;top:1122px;display:flex;justify-content:center;gap:46px;font-size:15px;color:var(--ink)}
  .footer .item{display:flex;align-items:center;gap:9px}
  .footer svg{width:22px;height:22px}
  .dot{width:16px;height:16px;border-radius:3px;background:var(--ink)}
</style>
</head>
<body>
<div class="poster">
  <div class="hero" role="img" aria-label="Group of paddlers on stand up paddle boards on a calm river with mangroves and sky"></div>

  <svg class="header-wave" viewBox="0 0 849 210" preserveAspectRatio="none" aria-hidden="true">
    <path d="M0 0H849V112C700 70 560 150 420 150C260 150 160 110 0 135Z" fill="var(--white)"/>
    <path d="M0 135C160 110 260 150 420 150C560 150 700 70 849 112V132C700 95 560 172 420 172C260 172 160 128 0 160Z" fill="var(--navy)"/>
    <path d="M0 160C160 128 260 172 420 172C560 172 700 95 849 132V140C700 110 560 186 420 186C260 186 160 140 0 170Z" fill="var(--blue)"/>
  </svg>

  <div class="brand">
    <span class="brand-mark"></span>
    <span class="brand-name">BRINKWAVE OAR</span>
  </div>

  <h1 class="headline">Explore the <strong>natural coastal</strong><br><strong>surroundings</strong> and <strong>waterways of Johor</strong><br>on a <strong>SUP adventure touring board</strong></h1>

  <div class="intro">
    <p>Our tours are flat-water and appropriate for all ages and levels. We have the best possible service and equipment. Join us for a fun and relaxing day.</p>
    <p>What could be better than a group guided tour? With life vests and a safety boat for our guided tour, you can be assured of a secured environment while you focus on just having fun and creating life's best memories with friends and family.</p>
  </div>

  <div class="gallery">
    <div class="photo p1" role="img" aria-label="Paddler on a river lined with mangrove trees"></div>
    <div class="photo p2" role="img" aria-label="Paddlers on open water under a bright sky"></div>
    <div class="photo p3" role="img" aria-label="Paddler on a yellow board near the riverbank"></div>
  </div>

  <div class="details">
    <p><b>TIMING:</b> Morning, Afternoon, and Sunset Session</p>
    <p><b>LOCATION:</b> Selwin River, set off from Tanjung Arlo, Pekan Rendah. (next to Pantai Mirah)</p>
  </div>

  <div class="contact-bar">Contact us for booking. We do not accept walk-in.</div>

  <div class="footer">
    <div class="item">
      <svg viewBox="0 0 24 24" aria-hidden="true"><rect x="2" y="5" width="20" height="14" rx="1.5" fill="none" stroke="var(--ink)" stroke-width="2"/><path d="M3 6l9 7 9-7" fill="none" stroke="var(--ink)" stroke-width="2"/></svg>
      <span>booking@brinkwaveoar.com.sg</span>
    </div>
    <div class="item">
      <span class="dot"></span>
      <span>Brinkwave Oar</span>
    </div>
    <div class="item">
      <svg viewBox="0 0 24 24" aria-hidden="true"><circle cx="12" cy="12" r="9" fill="none" stroke="var(--ink)" stroke-width="2"/><path d="M3 12h18M12 3c3 3 3 15 0 18M12 3c-3 3-3 15 0 18" fill="none" stroke="var(--ink)" stroke-width="1.6"/></svg>
      <span>www.brinkwaveoar.com.sg</span>
    </div>
  </div>
</div>
</body>
</html>
```